Summit Homes Collective Business Card

We are looking for a simple clean real estate business card design that includes the following information:

Front of card (2):

Front 1:

Photo of Brent (with the background cut out) on the front

Summit Logo at the top

Small Maple Keystone logo at the bottom

Brent Walkowicz
555.218.4036
BrentWalkowicz@MapleKeystone.example
#4, 2917 - 41Ave. Red Deer, Ab T0X 1Z0

Front 1:

Photo of Liam (with the background cut out) on the front

Summit Logo at the top

Liam Pettigrew
555.274.9180
LiamPettigrew@MapleKeystone.example

Back of card (for both cards):
**very simple and plain with the SUMMIT LOGO faded in the background**

Your Home Sold GUARANTEED Or We'll Buy It Or Sell It For Free...Your Choice

Buy Any Property With Us And If You're Not 100% Satisfied We'll Sell It For Free!

Industry/Entity Type

Real Estate

```html
<!DOCTYPE html>
<html lang="en">
<head>
<meta charset="utf-8">
<title>Summit Homes Collective – Business Cards</title>
<link rel="stylesheet" href="https://fonts.googleapis.com/css2?family=Open+Sans:wght@400;600;700&display=swap">
<style>
  :root {
    --stage: #a7a7a7;
    --card: #fbfbfb;
    --brand-red: #a3171b;
    --ink: #2f2f2f;
    --muted: #5a5a5a;
    --faint: #e9dcd9;
    --photo-top: #7b6a60;
    --photo-bottom: #2b2b2e;
  }
  * { box-sizing: border-box; margin: 0; padding: 0; }
  html, body { width: 1200px; height: 960px; overflow: hidden; }
  body {
    background: var(--stage);
    font-family: "Open Sans", Verdana, sans-serif;
    position: relative;
  }
  .card {
    position: absolute;
    background: var(--card);
    box-shadow: 0 3px 8px rgba(0,0,0,.35);
    overflow: hidden;
  }
  .card--brent { left: 86px; top: 338px; width: 346px; height: 558px; }
  .card--back  { left: 444px; top: 54px; width: 344px; height: 564px; }
  .card--liam  { left: 804px; top: 344px; width: 344px; height: 558px; }

  .brand {
    position: absolute;
    left: 0; right: 0;
    display: flex;
    align-items: center;
    justify-content: center;
    gap: 8px;
  }
  .brand__dot {
    width: 30px; height: 30px;
    border-radius: 50%;
    background: var(--brand-red);
  }
  .brand__name {
    font-weight: 700;
    font-size: 17px;
    letter-spacing: .5px;
    color: var(--brand-red);
    text-transform: uppercase;
  }
  .card--brent .brand { top: 56px; }
  .card--liam .brand  { top: 62px; }
  .card--back .brand  { top: 86px; }

  .portrait {
    position: absolute;
    left: 0; top: 0;
    width: 100%; height: 100%;
  }
  .portrait__stop-top { stop-color: var(--photo-top); }
  .portrait__stop-bottom { stop-color: var(--photo-bottom); }

  .agent {
    position: absolute;
    right: 32px;
    text-align: right;
    z-index: 1;
  }
  .agent__name {
    color: var(--brand-red);
    font-weight: 400;
    line-height: 1;
  }
  .agent__line {
    font-size: 9px;
    color: var(--ink);
    line-height: 1.65;
  }
  .card--brent .agent { top: 258px; }
  .card--brent .agent__name { font-size: 21px; margin-bottom: 12px; }
  .card--liam .agent { top: 268px; right: 28px; }
  .card--liam .agent__name { font-size: 17px; margin-bottom: 16px; }
  .card--liam .agent__line { line-height: 1.75; }

  .partner {
    position: absolute;
    font-size: 10px;
    font-weight: 700;
    color: var(--ink);
    text-transform: uppercase;
    line-height: 1.1;
  }
  .card--brent .partner { left: 238px; top: 506px; }
  .card--liam .partner  { left: 236px; top: 510px; }

  .back__mark {
    position: absolute;
    left: 48px; top: 160px;
    width: 246px; height: 246px;
    border-radius: 50%;
    background: var(--faint);
    opacity: .8;
  }
  .back__copy {
    position: absolute;
    left: 0; right: 0;
    top: 432px;
    text-align: center;
    font-size: 14px;
    line-height: 1.15;
    color: var(--muted);
    letter-spacing: .2px;
  }
  .back__copy p + p { margin-top: 10px; }
</style>
</head>
<body>

  <section class="card card--brent">
    <div class="brand">
      <span class="brand__dot"></span>
      <span class="brand__name">Summit Homes Collective</span>
    </div>
    <svg class="portrait" viewBox="0 0 346 558" role="img" aria-label="Cut-out portrait photo of Brent Walkowicz in a grey blazer and white shirt">
      <defs>
        <linearGradient id="brent-tone" x1="0" y1="0" x2="0" y2="1">
          <stop offset="0" class="portrait__stop-top"/>
          <stop offset="1" class="portrait__stop-bottom"/>
        </linearGradient>
      </defs>
      <path fill="url(#brent-tone)" d="M16 180 Q16 124 66 124 Q116 124 116 180 L116 352 L150 356 L202 410 L202 558 L0 558 L0 400 L16 380 Z"/>
    </svg>
    <div class="agent">
      <h2 class="agent__name">Brent Walkowicz</h2>
      <p class="agent__line">#4, 2917 - 41Ave. Red Deer, Ab T0X 1Z0</p>
      <p class="agent__line">555.218.4036</p>
      <p class="agent__line">BrentWalkowicz@MapleKeystone.example</p>
    </div>
    <div class="partner">Maple Keystone</div>
  </section>

  <section class="card card--back">
    <div class="brand">
      <span class="brand__dot"></span>
      <span class="brand__name">Summit Homes Collective</span>
    </div>
    <div class="back__mark" aria-hidden="true"></div>
    <div class="back__copy">
      <p>Your Home Sold GUARANTEED Or<br>We'll Buy It Or Sell It For Free...<br>Your Choice</p>
      <p>Buy Any Property With Us And<br>If You're Not 100% Satisfied<br>We'll Sell It For Free!</p>
    </div>
  </section>

  <section class="card card--liam">
    <div class="brand">
      <span class="brand__dot"></span>
      <span class="brand__name">Summit Homes Collective</span>
    </div>
    <svg class="portrait" viewBox="0 0 344 558" role="img" aria-label="Cut-out portrait photo of Liam Pettigrew in a black suit and white shirt">
      <defs>
        <linearGradient id="liam-tone" x1="0" y1="0" x2="0" y2="1">
          <stop offset="0" class="portrait__stop-top"/>
          <stop offset="1" class="portrait__stop-bottom"/>
        </linearGradient>
      </defs>
      <path fill="url(#liam-tone)" d="M18 196 Q18 140 68 140 Q118 140 118 196 L118 382 L160 386 L226 440 L226 558 L0 558 L0 420 L18 400 Z"/>
    </svg>
    <div class="agent">
      <h2 class="agent__name">Liam Pettigrew</h2>
      <p class="agent__line">555.274.9180</p>
      <p class="agent__line">LiamPettigrew@MapleKeystone.example</p>
      <p class="agent__line">#4, 2917 - 41Ave. Red Deer,<br>Ab T0X 1Z0</p>
    </div>
    <div class="partner">Maple Keystone</div>
  </section>

</body>
</html>
```